Business Card Design for Kestrelwood Carpentry

I need a business card design for my carpentry company Kestrelwood Carpentry. Ive attached files with all information I require on both sides. Look forward to seeing your design.

```html
<!DOCTYPE html>
<html lang="en">
<head>
<meta charset="utf-8">
<title>Kestrelwood Carpentry – Business Card</title>
<link rel="stylesheet" href="https://fonts.googleapis.com/css2?family=Lato:wght@400;700;900&display=swap">
<style>
  :root {
    --bg: #242220;
    --card: #ffffff;
    --ink: #1f1f22;
    --orange: #f05323;
    --muted: #333333;
  }
  * { box-sizing: border-box; margin: 0; padding: 0; }
  html, body { width: 1200px; height: 960px; overflow: hidden; background: var(--bg); }
  body { font-family: "Lato", sans-serif; color: var(--ink); }

  .sheet {
    width: 1200px; height: 960px;
    display: flex; flex-direction: column; align-items: center; justify-content: center;
    gap: 60px;
  }
  .card {
    width: 700px; height: 400px;
    background: var(--card);
    border-radius: 34px;
    position: relative;
    overflow: hidden;
    box-shadow: 0 14px 30px rgba(0,0,0,.45);
  }

  /* brand lockup */
  .brand { display: flex; flex-direction: column; align-items: center; }
  .brand-rule { width: 100%; height: 4px; background: var(--orange); }
  .brand-row { display: flex; align-items: center; gap: 14px; padding: 8px 0; }
  .brand-dot { width: 14px; height: 14px; border-radius: 50%; background: var(--orange); }
  .brand-name {
    font-weight: 900; font-size: 40px; letter-spacing: 2px; text-transform: uppercase;
    color: var(--ink); line-height: 1;
  }

  /* front */
  .card--front { display: flex; flex-direction: column; align-items: center; padding-top: 92px; }
  .card--front .brand { width: 560px; }
  .phone { display: flex; align-items: center; gap: 12px; margin-top: 28px;
    font-weight: 900; font-size: 36px; letter-spacing: 2px; }
  .phone svg { width: 30px; height: 30px; }
  .dots { display: flex; gap: 8px; margin-top: 18px; }
  .dots span { width: 9px; height: 9px; border-radius: 50%; background: var(--orange); }
  .tagline { margin-top: 16px; color: var(--orange); font-size: 27px; letter-spacing: 1px; }

  /* back */
  .card--back { padding-top: 30px; }
  .card--back .brand { width: 420px; margin: 0 auto; }
  .card--back .brand-name { font-size: 28px; }
  .licence { text-align: center; margin-top: 10px; font-weight: 900; font-size: 17px; letter-spacing: 1px; }
  .licence .lic-label { color: var(--orange); }
  .services { display: flex; justify-content: space-between; padding: 24px 36px 0; }
  .services ul { list-style: none; }
  .services li { display: flex; align-items: center; gap: 9px; font-size: 17px; color: var(--muted); line-height: 1.45; }
  .services li svg { width: 15px; height: 15px; flex: none; }
  .contact-band {
    position: absolute; left: 0; right: 0; bottom: 0; height: 74px;
    background: var(--orange);
    display: flex; align-items: center; justify-content: center; gap: 12px;
    color: #fff; font-size: 22px; letter-spacing: 1px;
  }
  .contact-band svg { width: 24px; height: 24px; }
</style>
</head>
<body>
<main class="sheet">

  <section class="card card--front">
    <div class="brand">
      <div class="brand-rule"></div>
      <div class="brand-row">
        <span class="brand-dot"></span>
        <span class="brand-name">Kestrelwood Carpentry</span>
      </div>
      <div class="brand-rule"></div>
    </div>
    <div class="phone">
      <svg viewBox="0 0 24 24" aria-hidden="true"><path fill="#1f1f22" d="M6.6 10.8a15.1 15.1 0 0 0 6.6 6.6l2.2-2.2c.3-.3.7-.4 1-.2 1.1.4 2.3.6 3.6.6.6 0 1 .4 1 1V20c0 .6-.4 1-1 1A17 17 0 0 1 3 4c0-.6.4-1 1-1h3.5c.6 0 1 .4 1 1 0 1.3.2 2.5.6 3.6.1.3 0 .7-.2 1z"/></svg>
      <span>041-555-0193</span>
    </div>
    <div class="dots"><span></span><span></span><span></span></div>
    <p class="tagline">Anything Carpentry, Anywhere in Sidney</p>
  </section>

  <section class="card card--back">
    <div class="brand">
      <div class="brand-rule"></div>
      <div class="brand-row">
        <span class="brand-dot"></span>
        <span class="brand-name">Kestrelwood Carpentry</span>
      </div>
      <div class="brand-rule"></div>
    </div>
    <p class="licence"><span class="lic-label">LIC# -</span> 904511K</p>

    <div class="services">
      <ul>
        <li><svg viewBox="0 0 16 16" aria-hidden="true"><rect x="1" y="1" width="14" height="14" fill="none" stroke="#1f1f22" stroke-width="1.5"/><path d="M4 8l3 3 6-7" fill="none" stroke="#f05323" stroke-width="2"/></svg>Decks and Pergolas</li>
        <li><svg viewBox="0 0 16 16" aria-hidden="true"><rect x="1" y="1" width="14" height="14" fill="none" stroke="#1f1f22" stroke-width="1.5"/><path d="M4 8l3 3 6-7" fill="none" stroke="#f05323" stroke-width="2"/></svg>Doors and Windows</li>
        <li><svg viewBox="0 0 16 16" aria-hidden="true"><rect x="1" y="1" width="14" height="14" fill="none" stroke="#1f1f22" stroke-width="1.5"/><path d="M4 8l3 3 6-7" fill="none" stroke="#f05323" stroke-width="2"/></svg>Attic conversions</li>
        <li><svg viewBox="0 0 16 16" aria-hidden="true"><rect x="1" y="1" width="14" height="14" fill="none" stroke="#1f1f22" stroke-width="1.5"/><path d="M4 8l3 3 6-7" fill="none" stroke="#f05323" stroke-width="2"/></svg>Wall Cladding</li>
      </ul>
      <ul>
        <li><svg viewBox="0 0 16 16" aria-hidden="true"><rect x="1" y="1" width="14" height="14" fill="none" stroke="#1f1f22" stroke-width="1.5"/><path d="M4 8l3 3 6-7" fill="none" stroke="#f05323" stroke-width="2"/></svg>Shop Fitouts</li>
        <li><svg viewBox="0 0 16 16" aria-hidden="true"><rect x="1" y="1" width="14" height="14" fill="none" stroke="#1f1f22" stroke-width="1.5"/><path d="M4 8l3 3 6-7" fill="none" stroke="#f05323" stroke-width="2"/></svg>Refurbishments</li>
        <li><svg viewBox="0 0 16 16" aria-hidden="true"><rect x="1" y="1" width="14" height="14" fill="none" stroke="#1f1f22" stroke-width="1.5"/><path d="M4 8l3 3 6-7" fill="none" stroke="#f05323" stroke-width="2"/></svg>Privacy Screens</li>
        <li><svg viewBox="0 0 16 16" aria-hidden="true"><rect x="1" y="1" width="14" height="14" fill="none" stroke="#1f1f22" stroke-width="1.5"/><path d="M4 8l3 3 6-7" fill="none" stroke="#f05323" stroke-width="2"/></svg>Extensions</li>
      </ul>
      <ul>
        <li><svg viewBox="0 0 16 16" aria-hidden="true"><rect x="1" y="1" width="14" height="14" fill="none" stroke="#1f1f22" stroke-width="1.5"/><path d="M4 8l3 3 6-7" fill="none" stroke="#f05323" stroke-width="2"/></svg>Wall and Roof Framing</li>
        <li><svg viewBox="0 0 16 16" aria-hidden="true"><rect x="1" y="1" width="14" height="14" fill="none" stroke="#1f1f22" stroke-width="1.5"/><path d="M4 8l3 3 6-7" fill="none" stroke="#f05323" stroke-width="2"/></svg>Fences / Gates</li>
        <li><svg viewBox="0 0 16 16" aria-hidden="true"><rect x="1" y="1" width="14" height="14" fill="none" stroke="#1f1f22" stroke-width="1.5"/><path d="M4 8l3 3 6-7" fill="none" stroke="#f05323" stroke-width="2"/></svg>Timber Flooring</li>
        <li><svg viewBox="0 0 16 16" aria-hidden="true"><rect x="1" y="1" width="14" height="14" fill="none" stroke="#1f1f22" stroke-width="1.5"/><path d="M4 8l3 3 6-7" fill="none" stroke="#f05323" stroke-width="2"/></svg>&amp; more</li>
      </ul>
    </div>

    <div class="contact-band">
      <svg viewBox="0 0 24 24" aria-hidden="true"><rect x="2" y="5" width="20" height="14" rx="1" fill="#1f1f22"/><path d="M2 6l10 7 10-7" fill="none" stroke="#fff" stroke-width="1.5"/></svg>
      <span>kestrelwoodcarpentry@mailbox.com</span>
    </div>
  </section>

</main>
</body>
</html>
```